Our Velvetline

I am developing a web site which sells preowned high end designer handbags and accessories. Some of the brands include: Duvore, Marcel Ostrand & Velka, to name a few. I am after a luxurious and high end feel.

Some brands I like that express this feel include: Corvin, Velka, thecloset-kip.com, pursetradeorloan.com

I am after a logo, business card, letterhead, with compliments, address label and envelope designs.
The business name is Our velvetline, and the website will be www.ourvelvetline.com.au. I have thoughts of using OVL as a logo or OUR velvetline.com.au

I don't want a large logo, it needs to blend in with the name in some way - or may not need an image at all, if the style of the font speaks to the brand.

Thank-you

Reason: I would like to give designers plenty of time to be able to submit a design.

Target Market(s)

Women, aged 25-60 who are into fashion

Industry/Entity Type

Business

Requirements
Must have
• High End
Luxurious

```html
<!DOCTYPE html>
<html lang="en">
<head>
<meta charset="utf-8">
<title>Our Velvetline — Stationery</title>
<link rel="stylesheet" href="https://fonts.googleapis.com/css2?family=Quicksand:wght@400;500&display=swap">
<style>
  :root {
    --backdrop: #e4e4e6;
    --velvet-deep: #3f1d66;
    --velvet: #5a2a8c;
    --velvet-glow: #7b45b0;
    --ribbon: #6a2fa0;
    --ribbon-sheer: rgba(214, 196, 235, 0.32);
    --paper: #ffffff;
    --paper-tint: #f6f4f8;
    --ink-brand: #5a2a8c;
    --ink-light: #efe6f8;
  }
  html, body {
    margin: 0;
    padding: 0;
    width: 1200px;
    height: 933px;
    overflow: hidden;
    background: var(--backdrop);
    font-family: "Quicksand", sans-serif;
  }
  .canvas {
    position: relative;
    width: 1200px;
    height: 933px;
    overflow: hidden;
  }

  /* shared pieces */
  .pattern-field {
    position: absolute;
    inset: 0;
  }
  .velvet-field {
    background: radial-gradient(ellipse at 40% 85%, var(--velvet-glow) 0%, var(--velvet) 45%, var(--velvet-deep) 100%);
  }
  .ribbon {
    position: absolute;
    left: 0;
    right: 0;
  }
  .brand-name {
    position: absolute;
    left: 0;
    right: 0;
    text-align: center;
    font-weight: 400;
    letter-spacing: 0.06em;
    white-space: nowrap;
  }

  /* letterhead */
  .letterhead {
    position: absolute;
    left: 610px;
    top: 60px;
    width: 560px;
    height: 792px;
    background: var(--paper);
    box-shadow: 0 2px 8px rgba(0,0,0,0.12);
    overflow: hidden;
  }
  .letterhead .pattern-field { background: var(--paper-tint); }
  .letterhead .brand-name {
    top: 34px;
    font-size: 26px;
    color: var(--ink-brand);
  }
  .letterhead .ribbon {
    top: 84px;
    height: 16px;
    background: var(--ribbon);
  }
  .letterhead-footer {
    position: absolute;
    left: 0;
    right: 0;
    bottom: 26px;
    display: flex;
    justify-content: center;
    gap: 34px;
    font-size: 11px;
    letter-spacing: 0.04em;
    color: var(--ink-brand);
  }

  /* business card */
  .business-card {
    position: absolute;
    left: 60px;
    top: 90px;
    width: 320px;
    height: 183px;
    overflow: hidden;
    box-shadow: 0 2px 8px rgba(0,0,0,0.18);
  }
  .business-card .brand-name {
    top: 26px;
    font-size: 17px;
    color: var(--ink-light);
  }
  .business-card .ribbon {
    top: 56px;
    height: 14px;
    background: var(--ribbon-sheer);
  }
  .card-holder {
    position: absolute;
    left: 16px;
    bottom: 16px;
    color: var(--ink-light);
  }
  .card-holder .holder-name { font-size: 13px; }
  .card-holder .holder-role {
    font-size: 6px;
    letter-spacing: 0.08em;
    margin-top: 2px;
  }
  .card-contact {
    position: absolute;
    right: 16px;
    bottom: 40px;
    font-size: 6.5px;
    line-height: 1.5;
    text-align: right;
    color: var(--ink-light);
  }

  /* envelope */
  .envelope {
    position: absolute;
    left: 60px;
    top: 420px;
    width: 520px;
    height: 260px;
    overflow: hidden;
    box-shadow: 0 2px 8px rgba(0,0,0,0.18);
  }
  .envelope .brand-name {
    top: 30px;
    font-size: 25px;
    color: var(--ink-light);
  }
  .envelope .ribbon {
    top: 76px;
    height: 22px;
    background: var(--ribbon-sheer);
  }
  .address-window {
    position: absolute;
    left: 58px;
    top: 144px;
    width: 276px;
    height: 82px;
    background: var(--paper);
    border-radius: 12px;
  }
  .envelope-footer {
    position: absolute;
    left: 58px;
    bottom: 12px;
    display: flex;
    gap: 24px;
    font-size: 10px;
    letter-spacing: 0.04em;
    color: var(--ink-light);
  }
</style>
</head>
<body>
<main class="canvas">

  <section class="business-card">
    <div class="pattern-field velvet-field" role="img" aria-label="Deep purple background with a faint lattice of small leaf motifs"></div>
    <div class="brand-name">Our Velvetline</div>
    <div class="ribbon"></div>
    <div class="card-holder">
      <div class="holder-name">Client Name</div>
      <div class="holder-role">DESIGNATION</div>
    </div>
    <div class="card-contact">
      12 Lindell Lane, Sydney<br>
      Phone: 02 5550 1843<br>
      Fax: 02 5550 1844
    </div>
  </section>

  <section class="envelope">
    <div class="pattern-field velvet-field" role="img" aria-label="Deep purple background with a faint lattice of small leaf motifs"></div>
    <div class="brand-name">Our Velvetline</div>
    <div class="ribbon"></div>
    <div class="address-window"></div>
    <div class="envelope-footer">
      <span>12 Lindell Lane, Sydney</span>
      <span>Phone: 02 5550 1843</span>
      <span>Fax: 02 5550 1844</span>
    </div>
  </section>

  <section class="letterhead">
    <div class="pattern-field" role="img" aria-label="White paper with a very faint lattice of small leaf motifs"></div>
    <div class="brand-name">Our Velvetline</div>
    <div class="ribbon"></div>
    <div class="letterhead-footer">
      <span>12 Lindell Lane, Sydney</span>
      <span>Phone: 02 5550 1843</span>
      <span>Fax: 02 5550 1844</span>
    </div>
  </section>

</main>
</body>
</html>
```